Velmira Home Page

I want to design a new home page using the look of two pages that I like.
http://us.dorazzi.com/
http://www.monvelle.us/?cm_mmc=searvo-_-EG_BR_Monvelle_Exact_CAR_D-_-Search-_-monvellehttp://us.dorazzi.com/
I like the framing of the dorazzi site and the drop down feel of the monvelle site. I will provide a new logo later today but for now can use what is already on my home page. The pictures in the middle of the page will rotate but I like the fonts and framing from Dorazzi.
My current site is www.velmira.com and I had a designer do a file which came close but missed the mark attached. This upscale and elegant
I liek the top log but would want the glass tilted to look liek the rest of the letters and in a grey or silver elegant color.
High end individuals andn corporations

```html
<!DOCTYPE html>
<html lang="en">
<head>
<meta charset="utf-8">
<title>Velmira — Home</title>
<link rel="stylesheet" href="https://fonts.googleapis.com/css2?family=Old+Standard+TT:wght@400;700&display=swap">
<style>
  :root {
    --ink-black: #000000;
    --text-white: #ffffff;
    --nav-muted: #cfc6bc;
    --band-dark: rgba(20, 12, 8, 0.55);
    --caption-dark: rgba(28, 20, 16, 0.72);
    --rule-light: rgba(255, 255, 255, 0.55);
    --dot-idle: rgba(255, 255, 255, 0.55);
    --social-grey: #8d8d8d;
    --hero-deep: #1e120b;
    --hero-warm: #6b4024;
    --hero-glow: #b97a45;
    --hero-cloth: #d8bfa2;
  }
  * { box-sizing: border-box; margin: 0; padding: 0; }
  html, body { width: 1200px; height: 900px; overflow: hidden; background: var(--ink-black); }
  body { font-family: "Old Standard TT", "Times New Roman", serif; color: var(--text-white); position: relative; }

  .hero {
    position: absolute; left: 0; top: 0; width: 1200px; height: 745px;
    background:
      radial-gradient(ellipse 55% 40% at 50% 45%, rgba(185,122,69,0.55), transparent 70%),
      radial-gradient(ellipse 60% 35% at 60% 95%, rgba(216,191,162,0.55), transparent 70%),
      linear-gradient(180deg, var(--hero-deep) 0%, var(--hero-warm) 38%, #8a5a36 60%, #5b3420 100%);
  }

  .brand {
    position: absolute; left: 42px; top: 36px;
    font-size: 55px; font-weight: 400; letter-spacing: 1px; line-height: 1;
  }
  .brand-divider {
    position: absolute; left: 335px; top: 28px; width: 1px; height: 77px;
    background: var(--rule-light);
  }
  .account-links {
    position: absolute; left: 356px; top: 31px; list-style: none;
    font-size: 14.5px; letter-spacing: 0.6px; line-height: 26px;
  }

  .social {
    position: absolute; right: 1px; top: 21px; list-style: none;
    display: flex; flex-direction: column; gap: 4px;
  }
  .social li { width: 20px; height: 20px; background: var(--social-grey); }

  .main-nav {
    position: absolute; left: 0; top: 135px; width: 1200px; height: 38px;
    background: var(--band-dark); border-top: 1px solid rgba(255,255,255,0.15);
  }
  .main-nav a {
    position: absolute; top: 10px; font-size: 14.5px; letter-spacing: 0.5px;
    color: var(--nav-muted); text-decoration: none;
  }
  .main-nav a.is-active { color: var(--text-white); }

  .gallery-caption {
    position: absolute; left: 386px; top: 400px; width: 475px; height: 80px;
    background: var(--caption-dark);
    display: flex; align-items: center; justify-content: center;
    font-size: 38px; letter-spacing: 0.5px;
  }

  .slide-dots {
    position: absolute; left: 1052px; top: 718px; display: flex; gap: 7px; list-style: none;
  }
  .slide-dots li { width: 11px; height: 11px; border-radius: 50%; background: var(--dot-idle); }
  .slide-dots li.is-current { background: var(--text-white); }

  .site-footer {
    position: absolute; left: 0; top: 745px; width: 1200px; height: 155px;
    background: var(--ink-black); text-align: center;
  }
  .services {
    margin-top: 24px; font-size: 17px; line-height: 22px; letter-spacing: 0.3px;
  }
  .copyright { position: absolute; left: 0; right: 0; top: 123px; font-size: 16.5px; }
</style>
</head>
<body>
  <div class="hero" role="img" aria-label="Photo of an elegant banquet hall with draped stage, podium, lanterns and long dressed tables"></div>

  <header>
    <div class="brand">VELMIRA</div>
    <div class="brand-divider"></div>
    <ul class="account-links">
      <li>MEMBER LOGIN</li>
      <li>JOIN OUR ENTOURAGE</li>
      <li>CONTACT US</li>
    </ul>
    <ul class="social" aria-label="Social links">
      <li></li><li></li><li></li><li></li>
    </ul>
  </header>

  <nav class="main-nav">
    <a style="left:42px">ENTOURAGE &amp; STAFFING</a>
    <a style="left:280px">EVENTS</a>
    <a style="left:390px">TRAVEL</a>
    <a class="is-active" style="left:498px">CELEBRITY &amp; PR</a>
    <a style="left:672px">OTHER SERVICES</a>
    <a style="left:848px">CLIENTS</a>
  </nav>

  <div class="gallery-caption">VIEW OUR GALLERY.</div>

  <ul class="slide-dots">
    <li class="is-current"></li><li></li><li></li><li></li><li></li><li></li>
  </ul>

  <footer class="site-footer">
    <p class="services">GRAND OPENINGS, TOURISM, RESORTS, RESTAURANTS, CHARITIES,<br>CORPORATE FUNCTIONS, PRIVATE EVENTS.</p>
    <p class="copyright">Copyright © Velmira LLC 2014.</p>
  </footer>
</body>
</html>
```